Wordpress Design for a Digital Management Consulting Business

I need a simple Wordpress Design and someone to set it up for a new boutique management consulting business called Tidewell Advisory that specialises in providing strategic advice to help grow digital businesses. It covers business strategy, marketing strategy, digital strategy, web product development, marketing campaigns, social, search, etc. From strategy to implementation.

URL is: tidewelladvisory.com.au

My professional background is here: au.examplenet.com/in/norabellweather

Competitors: other boutique digital/marketing management consulting businesses in Australia

The logos, colours and fonts are attached.

I would like the site to convey a business that is Smart/intelligent, Contemporary, Progressive, Digital, Energetic, Friendly.

The objective of the site is to educate visitors about what Tidewell Advisory does and encourage them to contact me for more information. It will be very light on content.

Target Market(s)

CEOs/Managing Directors, General Managers, Marketing Directors

Industry/Entity Type

Management Consulting

Font styles to use
Sans Serif

Colors
e34197
5c5c5c
000000

Requirements
Must have
• Site design requirements:
• Choose an appropriate Wordpress template, set it up for me and let me be able to edit it ongoing.
• It should use lots of images - these can be inspirational and not necessarily tied directly to the work
• Pink should feature, but not be the dominant colour.
• Site structure should be:
• 1. Home page - image led with horizontal navigation. Text beneath and images to describe the services.
• 2. About page - with space to write text and insert a picture of the Director
• 3. Services - with space to highlight services either as a list or graphically with text
• 4. Contact page - with space to write text and add email links, etc.
• Should have horizontal navigation
• It should have the flexibility to add another page
Nice to have
• Use the tree icon somehow in the design - consider in the background enlarged
• Use pink, grey, black from logo. Can introduce another complimentary colour if necessary.
• Can introduce another complimentary font to go with the logo font.
Should not have
• Use cliched business images and icons, eg. business suits, hand shakes, business men, business ties.

```html
<!DOCTYPE html>
<html lang="en">
<head>
<meta charset="utf-8">
<title>Tidewell Advisory</title>
<link rel="stylesheet" href="https://fonts.googleapis.com/css2?family=Raleway:wght@400;600;700;800&family=Open+Sans:wght@400;600&display=swap">
<style>
:root{
  --pink:#e34197;
  --pink-band:#d9408f;
  --grey:#5c5c5c;
  --dark:#1d1d1d;
  --ink:#333;
  --light:#f4f4f4;
  --white:#fff;
}
*{box-sizing:border-box;margin:0;padding:0}
html,body{width:1200px;height:2292px;overflow:hidden}
body{font-family:"Open Sans",Arial,sans-serif;color:var(--ink);background:var(--white);position:relative}
.heading{font-family:"Raleway",Arial,sans-serif}

/* header */
.site-header{position:absolute;top:0;left:0;width:1200px;height:78px;background:var(--white);display:flex;align-items:center;justify-content:space-between;padding:0 30px 0 24px;border-bottom:1px solid #eee}
.brand{display:flex;align-items:center;gap:10px;font-family:"Raleway",sans-serif;font-weight:700;font-size:26px;color:var(--pink);letter-spacing:.5px}
.brand-dot{width:26px;height:26px;border-radius:50%;background:var(--pink)}
.main-nav{display:flex;gap:6px}
.main-nav a{font-family:"Raleway",sans-serif;font-size:13px;font-weight:600;color:var(--grey);text-decoration:none;padding:10px 16px;letter-spacing:.5px}
.main-nav a.active{color:var(--pink);border-bottom:2px solid var(--pink)}

/* hero */
.hero{position:absolute;top:78px;left:0;width:1200px;height:548px;overflow:hidden}
.hero-photo{position:absolute;inset:0;background:linear-gradient(100deg,#c9cdd2 0%,#e7e4e1 30%,#f3f2f0 55%,#dfe3e8 100%)}
.hero-copy{position:absolute;left:690px;top:150px;width:400px;text-align:center}
.hero-copy h1{font-family:"Raleway",sans-serif;font-weight:800;font-size:62px;color:var(--pink);letter-spacing:2px;line-height:1}
.hero-copy h2{font-family:"Raleway",sans-serif;font-weight:700;font-size:15px;color:#444;margin-top:10px;letter-spacing:.5px}
.hero-copy p{font-size:12px;line-height:1.55;color:#555;margin-top:10px}
.btn-dark{display:inline-block;background:#333;color:var(--white);font-size:13px;padding:9px 20px;border-radius:3px;text-decoration:none}
.hero-copy .btn-dark{margin-top:140px}
.hero-dots{position:absolute;left:0;right:0;bottom:16px;display:flex;justify-content:center;gap:8px}
.hero-dots span{width:9px;height:9px;border-radius:50%;background:#fff;opacity:.7}
.hero-dots span.on{background:var(--pink);opacity:1}

/* section titles */
.section-title{display:flex;align-items:center;justify-content:center;gap:18px;font-family:"Raleway",sans-serif;font-weight:600;font-size:22px;letter-spacing:1px}
.section-title::before,.section-title::after{content:"";width:70px;height:2px;background:currentColor;opacity:.8}

/* who we are */
.who{position:absolute;top:626px;left:0;width:1200px;height:384px;background:var(--light);text-align:center}
.who .section-title{color:var(--pink);margin-top:70px}
.who p{width:1150px;margin:40px auto 0;font-size:15px;line-height:1.6;color:#555;text-align:left}
.who .btn-dark{margin-top:48px;padding:11px 22px;font-size:15px;background:#3a3a3a}

/* services */
.services{position:absolute;top:1010px;left:0;width:1200px;height:548px;background:var(--pink-band);color:var(--white)}
.services .section-title{margin-top:62px;color:var(--white)}
.service-grid{display:flex;justify-content:space-between;width:1090px;margin:48px auto 0}
.service{width:280px;text-align:center}
.service-img{width:280px;height:165px;border:5px solid #fff;box-shadow:0 2px 6px rgba(0,0,0,.2)}
.service-img.s1{background:linear-gradient(135deg,#2d3e55,#8aa4c0 60%,#d9e2ec)}
.service-img.s2{background:linear-gradient(135deg,#f1eef0,#cfd6dd 50%,#e8a2c7)}
.service-img.s3{background:linear-gradient(135deg,#a7b0ba,#e9ecef 55%,#6d7884)}
.service h3{font-family:"Raleway",sans-serif;font-weight:700;font-size:19px;margin-top:20px}
.service p{font-size:12.5px;line-height:1.5;margin:10px auto 0;width:220px}
.btn-light{display:inline-block;background:#fff;color:#333;font-size:12.5px;padding:7px 16px;border-radius:3px;margin-top:26px;text-decoration:none}

/* what we do */
.what{position:absolute;top:1558px;left:0;width:1200px;height:432px;background:var(--white);overflow:hidden}
.what-photo{position:absolute;left:0;bottom:0;width:1200px;height:200px;background:linear-gradient(180deg,rgba(255,255,255,1) 0%,rgba(210,212,215,.7) 60%,#9fa3a8 100%)}
.what .section-title{position:relative;color:var(--pink);margin-top:42px}
.what-grid{position:relative;display:flex;justify-content:space-between;width:1120px;margin:42px auto 0}
.what-item{width:300px;text-align:center}
.what-icon{width:86px;height:86px;margin:0 auto}
.what-item h3{font-family:"Raleway",sans-serif;font-weight:600;font-size:20px;color:#222;margin-top:18px}
.what-item p{font-size:12.5px;line-height:1.5;color:#333;width:220px;margin:18px auto 0}

/* footer */
.site-footer{position:absolute;top:1990px;left:0;width:1200px;height:302px;background:#151515;color:#ccc;display:flex;padding:26px 50px 0 50px}
.footer-col h4{font-family:"Raleway",sans-serif;font-weight:400;font-size:22px;color:#eee;margin-bottom:22px}
.footer-col ul{list-style:none}
.footer-col li{font-size:11.5px;line-height:1;margin-bottom:14px;color:#bbb}
.footer-col li::before{content:"›";color:var(--pink);margin-right:8px}
.col-links{width:190px}
.col-services{width:470px;border-left:1px solid #333;padding-left:24px}
.col-services .lists{display:flex;gap:50px}
.col-follow{width:140px;border-left:1px solid #333;padding-left:24px}
.social{display:flex;flex-direction:column;gap:12px;padding-left:14px}
.social span{width:22px;height:22px;border-radius:50%;background:#777}
.col-contact{border-left:1px solid #333;padding-left:24px;width:240px}
.col-contact p{font-size:11.5px;line-height:1.6;color:#bbb;margin-bottom:10px}
.contact-row{display:flex;align-items:center;gap:8px;font-size:11.5px;color:#bbb;margin-bottom:10px}
.contact-row svg{flex:none}
</style>
</head>
<body>

<header class="site-header">
  <div class="brand"><span class="brand-dot"></span>Tidewell Advisory</div>
  <nav class="main-nav">
    <a class="active" href="#">HOME</a>
    <a href="#">ABOUT US</a>
    <a href="#">SERVICES</a>
    <a href="#">PROJECTS</a>
    <a href="#">NEWS</a>
    <a href="#">CONTACT</a>
  </nav>
</header>

<section class="hero">
  <div class="hero-photo" role="img" aria-label="Photo of people working at computers in a bright office"></div>
  <div class="hero-copy">
    <h1>ACHIEVE</h1>
    <h2>YOUR GOALS AND LONG TERM SUCCESS</h2>
    <p>Clear strategy turns ambition into progress. We help digital businesses plan, launch and grow with focus, measurable goals and practical steps that lead from first idea to lasting results.</p>
    <a class="btn-dark" href="#">Read More</a>
  </div>
  <div class="hero-dots"><span class="on"></span><span></span><span></span></div>
</section>

<section class="who">
  <h2 class="section-title">WHO WE ARE</h2>
  <p>Tidewell Advisory is a boutique management consulting company advising digital businesses across business, product and marketing strategy. Combining strategic thinking with digital know-how and marketing expertise Tidewell Advisory works with businesses looking to develop their digital capabilities or wanting to accelerate the growth of a new or existing digital business.</p>
  <a class="btn-dark" href="#">Click to know more...</a>
</section>

<section class="services">
  <h2 class="section-title">OUR SERVICES</h2>
  <div class="service-grid">
    <div class="service">
      <div class="service-img s1" role="img" aria-label="Image of hands using a glowing digital network interface"></div>
      <h3>DIGITAL STRATEGY</h3>
      <p>Loremipsum dolor sit amet, consect etuasdy sumgelit, sed do eius mod tempores i dol uttdl aboredidolore magna aliqua.</p>
      <a class="btn-light" href="#">Read More</a>
    </div>
    <div class="service">
      <div class="service-img s2" role="img" aria-label="Image of a marketing strategy sketch on a whiteboard"></div>
      <h3>MARKETING STRATEGY</h3>
      <p>Loremipsum dolor sit amet, consect etuasdy sumgelit, sed do eius mod tempores i dol uttdl aboredidolore magna aliqua.</p>
      <a class="btn-light" href="#">Read More</a>
    </div>
    <div class="service">
      <div class="service-img s3" role="img" aria-label="Image of a laptop and digital devices on a desk"></div>
      <h3>DIGITAL TRANSFORMATION</h3>
      <p>Loremipsum dolor sit amet, consect etuasdy sumgelit, sed do eius mod tempores i dol uttdl aboredidolore magna aliqua.</p>
      <a class="btn-light" href="#">Read More</a>
    </div>
  </div>
</section>

<section class="what">
  <div class="what-photo" role="img" aria-label="Faded photo of a team meeting around a table"></div>
  <h2 class="section-title">WHAT WE DO</h2>
  <div class="what-grid">
    <div class="what-item">
      <svg class="what-icon" viewBox="0 0 86 86" aria-hidden="true">
        <circle cx="43" cy="43" r="43" fill="#e34197"/>
        <circle cx="43" cy="38" r="14" fill="none" stroke="#fff" stroke-width="4"/>
        <rect x="36" y="54" width="14" height="5" rx="1" fill="#fff"/>
        <rect x="38" y="61" width="10" height="4" rx="1" fill="#fff"/>
      </svg>
      <h3>Strategic Thinking</h3>
      <p>Loremipsum dolor sit amet, consect etuasdy sumgelit, sed do eius mod tempores i dol uttdl aboredidolore magna aliqua.</p>
    </div>
    <div class="what-item">
      <svg class="what-icon" viewBox="0 0 86 86" aria-hidden="true">
        <circle cx="43" cy="43" r="43" fill="#e34197"/>
        <rect x="24" y="46" width="9" height="16" fill="#fff"/>
        <rect x="38" y="36" width="9" height="26" fill="#fff"/>
        <rect x="52" y="26" width="9" height="36" fill="#fff"/>
      </svg>
      <h3>Analytical Approach</h3>
      <p>Loremipsum dolor sit amet, consect etuasdy sumgelit, sed do eius mod tempores i dol uttdl aboredidolore magna aliqua.</p>
    </div>
    <div class="what-item">
      <svg class="what-icon" viewBox="0 0 86 86" aria-hidden="true">
        <circle cx="43" cy="43" r="43" fill="#e34197"/>
        <circle cx="43" cy="43" r="18" fill="none" stroke="#fff" stroke-width="4"/>
        <path d="M34 43l6 6 12-12" fill="none" stroke="#fff" stroke-width="4" stroke-linecap="round" stroke-linejoin="round"/>
      </svg>
      <h3>End to End Project Management</h3>
      <p>Loremipsum dolor sit amet, consect etuasdy sumgelit, sed do eius mod tempores i dol uttdl aboredidolore magna aliqua.</p>
    </div>
  </div>
</section>

<footer class="site-footer">
  <div class="footer-col col-links">
    <h4>Quick Links</h4>
    <ul><li>Home</li><li>About Us</li><li>Projects</li><li>News</li><li>Contacts</li></ul>
  </div>
  <div class="footer-col col-services">
    <h4>Services</h4>
    <div class="lists">
      <ul><li>Business Strategy</li><li>Digital Strategy</li><li>Marketing Strategy</li><li>Product Strategy</li><li>Marketing Campaigns</li></ul>
      <ul><li>Product Management</li><li>Digital Marketing</li><li>Sales CRM Strategy</li><li>Content Marketing</li><li>New Product Launches</li></ul>
    </div>
  </div>
  <div class="footer-col col-follow">
    <h4>Follow Us</h4>
    <div class="social"><span></span><span></span><span></span><span></span></div>
  </div>
  <div class="footer-col col-contact">
    <h4>Contact Details</h4>
    <p>For more information about what we do please contact:<br>Nora Bellweather</p>
    <div class="contact-row">
      <svg width="16" height="16" viewBox="0 0 16 16" aria-hidden="true"><circle cx="8" cy="8" r="8" fill="#e34197"/><path d="M5 4.5l1.5-.5 1 2-1 .8a5 5 0 0 0 2.7 2.7l.8-1 2 1-.5 1.5C8.5 11.5 4.5 7.5 5 4.5z" fill="#fff"/></svg>
      0400 555 019
    </div>
    <div class="contact-row">
      <svg width="16" height="16" viewBox="0 0 16 16" aria-hidden="true"><circle cx="8" cy="8" r="8" fill="#e34197"/><rect x="4" y="5" width="8" height="6" fill="none" stroke="#fff" stroke-width="1.2"/><path d="M4 5l4 3.5L12 5" fill="none" stroke="#fff" stroke-width="1.2"/></svg>
      nora@tidewelladvisory.com.au
    </div>
  </div>
</footer>

</body>
</html>
```